Velvetorchid Hair & Beauty Business Card

Velvetorchid Hair & Beauty is a boutique salon located in the picturesque Lake Taupo NZ. The salon is very luxurious, opulent gold gilded mirrors, chandelier lit, contemporary french decor, sets the mood to create beautiful hair, makeup and all beauty services. Just had a new logo design and now after a new business card.
Logo
14 Korowhai Street
Taupo
Phone (07) 548 6193
www.velvetorchid.co.nz
email hair@velvetorchid.co.nz
Marlena Swithin
Also need a space to put in Stylist name, date, appointment time. thanks;)
Another idea is we could incorporate the wallpaper in the back ground either on the back or front or use an ornate glided frame (around the edge of the card) like on my website where my brides photos flash.
Decided against the wall paper but at least you can see our colour theme for the salon.
Updates

Please check out my updated brief . Thanks :)

Target Market(s)

25-60 years plus, mainly mid age females , wanting the best possible service , high standard of workmanship and money not a problem.

Industry/Entity Type

Boutique

Requirements
Must have
• Gold and silver

```html
<!DOCTYPE html>
<html lang="en">
<head>
<meta charset="utf-8">
<title>Velvetorchid Hair &amp; Beauty – Cards</title>
<link href="https://fonts.googleapis.com/css2?family=Quicksand:wght@400;500&display=swap" rel="stylesheet">
<style>
  :root {
    --stage: #eee9e1;
    --card: #ffffff;
    --ink-grey: #5e5e5e;
    --gold: #8a7424;
    --gold-soft: #b9a25a;
    --gold-pale: #e6dcc2;
    --rule: #ddd2bd;
    --frame-light: #ede2c8;
    --frame-mid: #d8c7a2;
    --frame-dark: #b6a27a;
    --face: #f7f2ea;
  }
  * { box-sizing: border-box; margin: 0; padding: 0; }
  html, body { width: 1200px; height: 1000px; overflow: hidden; }
  body {
    background: var(--stage);
    font-family: "Quicksand", sans-serif;
    position: relative;
  }

  /* ---------- shared brand lockup ---------- */
  .brand-name {
    color: var(--ink-grey);
    font-weight: 400;
    text-align: center;
    letter-spacing: -0.5px;
    line-height: 1;
  }
  .brand-tagline {
    display: flex;
    align-items: center;
    gap: 10px;
    color: var(--gold);
    font-weight: 400;
    text-transform: uppercase;
  }
  .brand-tagline .rule { flex: 1; height: 2px; background: var(--gold); }

  .ornament {
    position: absolute;
    border-radius: 40% 40% 50% 50% / 60% 60% 40% 40%;
  }

  /* ---------- appointment card ---------- */
  .appointment-card {
    position: absolute;
    left: 140px; top: 106px;
    width: 418px; height: 626px;
    background: var(--card);
    box-shadow: 0 2px 6px rgba(0,0,0,.12);
  }
  .appointment-card .ornament-top {
    left: 70px; top: 24px; width: 268px; height: 62px;
    background: radial-gradient(ellipse at center, var(--gold-soft) 0%, var(--gold-pale) 70%, transparent 100%);
  }
  .appointment-card .brand-name {
    position: absolute; left: 0; right: 0; top: 96px;
    font-size: 50px;
  }
  .appointment-card .brand-tagline {
    position: absolute; left: 33px; right: 42px; top: 150px;
    font-size: 14px;
  }
  .appointment-title {
    position: absolute; left: 0; right: 0; top: 176px;
    text-align: center;
    font-size: 24px;
    color: var(--ink-grey);
  }
  .booking-field {
    position: absolute; left: 35px; right: 64px;
    display: flex; align-items: flex-end; gap: 14px;
    color: var(--gold);
    font-size: 23px;
    text-transform: uppercase;
    letter-spacing: -0.5px;
  }
  .booking-field .write-line { flex: 1; height: 1px; background: var(--rule); margin-bottom: 6px; }
  .booking-field.name { top: 238px; }
  .booking-field.date { top: 332px; }
  .booking-field.time { top: 426px; }
  .extra-line {
    position: absolute; left: 55px; right: 64px; height: 1px; background: var(--rule);
  }
  .extra-line.after-name { top: 300px; }
  .extra-line.after-date { top: 403px; }
  .appointment-card .ornament-bottom {
    left: 6px; top: 498px; width: 352px; height: 116px;
    background: radial-gradient(ellipse at center, var(--gold-pale) 0%, #f3eee2 65%, transparent 100%);
  }

  /* ---------- business card ---------- */
  .business-card {
    position: absolute;
    left: 508px; top: 470px;
    width: 626px; height: 418px;
    background: linear-gradient(135deg, var(--frame-light), var(--frame-mid) 50%, var(--frame-light));
    box-shadow: 0 3px 8px rgba(0,0,0,.18);
  }
  .gilded-border {
    position: absolute; inset: 18px;
    border: 6px double var(--frame-dark);
  }
  .card-face {
    position: absolute; left: 36px; top: 36px; right: 36px; bottom: 36px;
    background: var(--face);
    border: 2px solid var(--frame-dark);
  }
  .business-card .ornament-top {
    left: 170px; top: 55px; width: 290px; height: 76px;
    background: radial-gradient(ellipse at center, var(--gold-soft) 0%, var(--gold-pale) 70%, transparent 100%);
  }
  .business-card .brand-name {
    position: absolute; left: 100px; right: 100px; top: 146px;
    font-size: 54px;
  }
  .business-card .brand-tagline {
    position: absolute; left: 125px; right: 124px; top: 218px;
    font-size: 17px;
  }
  .contact-details {
    position: absolute; left: 50px; top: 262px; width: 280px;
    text-align: center;
    color: var(--ink-grey);
    font-weight: 500;
    line-height: 1.25;
  }
  .contact-details .address, .contact-details .phone { font-size: 20px; }
  .contact-details .web, .contact-details .email { font-size: 19px; }
  .owner {
    position: absolute; right: 60px; top: 288px; width: 210px;
    text-align: right;
  }
  .owner .owner-name { font-size: 21px; color: var(--ink-grey); font-weight: 500; }
  .owner .owner-role {
    display: flex; align-items: center; gap: 8px; justify-content: flex-end;
    margin-top: 8px;
    font-size: 15px; color: var(--gold); text-transform: uppercase;
  }
  .owner .owner-role .rule { width: 52px; height: 1px; background: var(--gold); }
</style>
</head>
<body>

  <section class="appointment-card" aria-label="Appointment card">
    <div class="ornament ornament-top" role="img" aria-label="Gold baroque scroll ornament"></div>
    <div class="brand-name">Velvetorchid</div>
    <div class="brand-tagline"><span class="rule"></span>Hair &amp; Beauty<span class="rule"></span></div>
    <div class="appointment-title">Appointment</div>

    <div class="booking-field name"><span>Name:</span><span class="write-line"></span></div>
    <div class="extra-line after-name"></div>
    <div class="booking-field date"><span>Date:</span><span class="write-line"></span></div>
    <div class="extra-line after-date"></div>
    <div class="booking-field time"><span>Time:</span><span class="write-line"></span></div>

    <div class="ornament ornament-bottom" role="img" aria-label="Faint gold baroque scroll ornament"></div>
  </section>

  <section class="business-card" aria-label="Business card">
    <div class="gilded-border"></div>
    <div class="card-face"></div>
    <div class="ornament ornament-top" role="img" aria-label="Gold baroque scroll ornament"></div>
    <div class="brand-name">Velvetorchid</div>
    <div class="brand-tagline"><span class="rule"></span>Hair &amp; Beauty<span class="rule"></span></div>

    <address class="contact-details" style="font-style: normal;">
      <div class="address">14 Korowhai Street, Taupo</div>
      <div class="phone">(07) 548 6193</div>
      <div class="web">www.velvetorchid.co.nz</div>
      <div class="email">hair@velvetorchid.co.nz</div>
    </address>

    <div class="owner">
      <div class="owner-name">Marlena Swithin</div>
      <div class="owner-role"><span class="rule"></span>Stylist &amp; Owner</div>
    </div>
  </section>

</body>
</html>
```